Product flyer with pricing

We manufacture iconic and luxury vending trailers. for our first trailer we need a flyer created to give to prospective clients with base pricing. I am uploading an example along with graphic files.

```html
<!DOCTYPE html>
<html lang="en">
<head>
<meta charset="utf-8">
<title>Luxury Vending Trailers Flyer</title>
<link href="https://fonts.googleapis.com/css2?family=Oswald:wght@500;600&family=Source+Sans+3:wght@400;600;700&display=swap" rel="stylesheet">
<style>
  :root {
    --green: #2f9a3c;
    --green-dark: #1f8a35;
    --green-light: #7cc242;
    --orange: #f0a92a;
    --orange-soft: #f7d08a;
    --ink: #333333;
    --grey: #666666;
    --rule: #cfcfcf;
    --page: #ffffff;
    --backdrop: #ececec;
  }
  * { box-sizing: border-box; margin: 0; padding: 0; }
  html, body { width: 1200px; height: 863px; overflow: hidden; }
  body { background: var(--backdrop); font-family: "Source Sans 3", sans-serif; color: var(--ink); position: relative; }

  .flyer {
    position: absolute; left: 280px; top: 18px;
    width: 612px; height: 790px;
    background: var(--page);
    transform: scale(1.046); transform-origin: top left;
    box-shadow: 0 2px 10px rgba(0,0,0,.15);
    overflow: hidden;
  }
  .hero { position: absolute; left: 0; top: 0; width: 612px; height: 420px; }

  .brand {
    position: absolute; right: 18px; top: 58px;
    display: flex; align-items: center; gap: 8px;
    font-weight: 700; font-size: 21px; line-height: 23px; letter-spacing: .5px;
    color: var(--green); text-align: right;
  }
  .brand-dot { width: 16px; height: 16px; border-radius: 50%; background: var(--orange); flex: none; }

  .headline {
    position: absolute; right: 18px; top: 180px; text-align: right;
    font-family: "Oswald", sans-serif; font-weight: 600;
    font-size: 34px; line-height: 39px; letter-spacing: .5px;
  }
  .headline .luxury { color: var(--orange); }
  .headline .vending, .headline .trailers { color: var(--green); }

  .product-title {
    position: absolute; left: 0; width: 612px; top: 406px; text-align: center;
    padding-left: 30px;
    font-weight: 700; font-size: 28px; color: var(--green-dark);
  }
  .product-sub {
    position: absolute; left: 0; width: 612px; top: 442px; text-align: center;
    padding-left: 30px;
    font-weight: 600; font-size: 15px; letter-spacing: 3.6px; color: var(--grey);
  }

  .uses { position: absolute; left: 26px; top: 482px; width: 444px; list-style: none; }
  .uses li {
    display: flex; align-items: center; gap: 6px;
    height: 23px; font-size: 12px; color: var(--ink);
    border-bottom: 1px dotted var(--rule);
  }
  .uses li:last-child { border-bottom: none; }
  .uses svg { width: 17px; height: 15px; flex: none; }
  .uses b { color: var(--green); font-weight: 700; }

  .price-badge { position: absolute; left: 467px; top: 457px; width: 120px; height: 120px; }
  .price-badge .label, .price-badge .amount { position: absolute; left: 0; width: 120px; text-align: center; color: #fff; }
  .price-badge .label { top: 41px; font-size: 11px; font-weight: 700; letter-spacing: .5px; }
  .price-badge .amount { top: 54px; font-size: 22px; font-weight: 700; }
  .price-badge .amount sup { font-size: 11px; vertical-align: 9px; }

  .tab {
    position: absolute; top: 590px; height: 22px;
    background: var(--orange); color: #fff;
    font-weight: 700; font-size: 13px; line-height: 22px;
    clip-path: polygon(0 0, 94% 0, 100% 100%, 0 100%);
  }
  .tab.features { left: 0; width: 216px; padding-left: 30px; }
  .tab.options { left: 328px; width: 236px; padding-left: 27px; clip-path: polygon(0 0, 94% 0, 100% 100%, 5% 100%); }

  .spec-list { position: absolute; top: 621px; list-style: none; font-size: 8.6px; line-height: 11px; color: var(--ink); }
  .spec-list li { position: relative; padding-left: 14px; margin-bottom: 3px; }
  .spec-list li::before {
    content: ""; position: absolute; left: 2px; top: 2px;
    width: 7px; height: 7px; border-radius: 50%; background: var(--orange);
  }
  .spec-list.features { left: 26px; width: 300px; }
  .spec-list.options { left: 334px; width: 275px; }
  .spec-list .cost { color: var(--green); font-weight: 700; }

  .contact-bar {
    position: absolute; left: 0; top: 746px; width: 612px; height: 44px;
    background: linear-gradient(90deg, var(--green), var(--green-light));
    display: flex; align-items: center; justify-content: space-between;
    padding: 0 30px 0 24px; color: #fff; font-size: 14px; font-weight: 600;
  }
  .contact-bar .item { display: flex; align-items: center; gap: 6px; }
  .contact-bar svg { width: 13px; height: 13px; }
</style>
</head>
<body>
<main class="flyer">

  <svg class="hero" viewBox="0 0 612 420">
    <defs>
      <linearGradient id="sky" x1="0" y1="0" x2="0" y2="1">
        <stop offset="0" stop-color="#8fb8e0"/>
        <stop offset=".45" stop-color="#e9eef2"/>
        <stop offset=".75" stop-color="#f4f4f4"/>
        <stop offset="1" stop-color="#6e7278"/>
      </linearGradient>
      <clipPath id="heroClip"><circle cx="190" cy="182" r="203"/></clipPath>
    </defs>
    <circle cx="190" cy="182" r="208" fill="none" stroke="var(--green)" stroke-width="8"/>
    <g role="img" aria-label="Photo of the white board-and-batten tiny farmhouse trailer parked on a lot">
      <rect x="0" y="0" width="612" height="420" fill="url(#sky)" clip-path="url(#heroClip)"/>
    </g>
    <circle cx="362" cy="282" r="98" fill="var(--orange-soft)"/>
    <g role="img" aria-label="Photo of the trailer side with serving window and tandem wheels">
      <circle cx="362" cy="282" r="86" fill="url(#sky)" stroke="#fff" stroke-width="3"/>
    </g>
    <circle cx="240" cy="334" r="74" fill="#fff"/>
    <g role="img" aria-label="Photo of the trailer front with door">
      <circle cx="240" cy="334" r="68" fill="url(#sky)"/>
    </g>
    <circle cx="112" cy="345" r="62" fill="#fff"/>
    <g role="img" aria-label="Photo of the trailer from the rear corner">
      <circle cx="112" cy="345" r="56" fill="url(#sky)"/>
    </g>
  </svg>

  <div class="brand"><span class="brand-dot"></span><span>BRIGHT ACRE<br>BUILDS</span></div>

  <h1 class="headline">
    <span class="luxury">LUXURY</span><br>
    <span class="vending">VENDING</span><br>
    <span class="trailers">TRAILERS</span>
  </h1>

  <h2 class="product-title">The “Prairie Porch Mini”</h2>
  <p class="product-sub">LUXURY, MOBILE VENDING HOUSE</p>

  <ul class="uses">
    <li>
      <svg viewBox="0 0 17 15"><path d="M2 4h10v6a3 3 0 0 1-3 3H5a3 3 0 0 1-3-3z M12 6h2a2 2 0 0 1 0 4h-2" fill="var(--orange)" stroke="var(--orange)" stroke-width="1.2"/><rect x="0" y="13" width="15" height="2" fill="var(--orange)"/></svg>
      <span><b>FOOD:</b> Lemonade, Coffee, pizza, cookies, doughnuts, barbecue and more!</span>
    </li>
    <li>
      <svg viewBox="0 0 17 15"><path d="M8.5 1L1 8h2.5v6h4v-4h2v4h4V8H16z" fill="var(--orange)"/></svg>
      <span><b>RETAIL:</b> Clothing, watches, jewelry, flowers and more!</span>
    </li>
    <li>
      <svg viewBox="0 0 17 15"><path d="M1 6l4-2 3.5 2 3.5-2 4 2-3 4-4.5 3-4.5-3z" fill="var(--orange)"/></svg>
      <span><b>CORPORATE:</b> Product info, demonstration, information, brand awareness.</span>
    </li>
    <li>
      <svg viewBox="0 0 17 15"><path d="M4 1h9v6a4.5 4.5 0 0 1-9 0z" fill="var(--orange)"/><circle cx="8.5" cy="6" r="2" fill="#fff"/></svg>
      <span><b>FUNDRAISERS:</b> Girls/boy sports, non profits, etc.</span>
    </li>
  </ul>

  <div class="price-badge">
    <svg viewBox="0 0 120 120" width="120" height="120">
      <circle cx="60" cy="60" r="57" fill="none" stroke="var(--green-light)" stroke-width="6" stroke-dasharray="3 3"/>
      <circle cx="60" cy="60" r="55" fill="var(--green-light)"/>
      <circle cx="60" cy="60" r="55" fill="var(--green)" opacity=".35"/>
    </svg>
    <div class="label">BASE PRICE:</div>
    <div class="amount"><sup>$</sup>45,000</div>
  </div>

  <div class="tab features">BASE UNIT FEATURES:</div>
  <div class="tab options">AVAILABLE OPTIONS:</div>

  <ul class="spec-list features">
    <li>Trailer features tandem wheels w/ brakes</li>
    <li>Steel frame construction for fire retardation safety &amp; weight reduction</li>
    <li>100% off grid with solar and lithium battery system allowing the trailer to be used in places not accessible by traditional trailers</li>
    <li>80 gallon water supply tank</li>
    <li>100 gallon waste water tank</li>
    <li>Cupboards, cabinets &amp; four stainless steel sinks</li>
    <li>60” Gas shock serving window</li>
  </ul>

  <ul class="spec-list options">
    <li>HVAC - Northwind Mini Split - <span class="cost">$1,800</span></li>
    <li>Cooler / Glass front Commercial refrigerator - <span class="cost">$1,600</span></li>
    <li>Upper loft storage area - <span class="cost">$1,200</span></li>
    <li>Signage and graphics - <span class="cost">$2,000 - $5,000</span> depend on complexity</li>
    <li>Ice machine - <span class="cost">$1,100</span></li>
    <li>Other custom items available on request.</li>
  </ul>

  <footer class="contact-bar">
    <span class="item">
      <svg viewBox="0 0 13 13"><circle cx="6.5" cy="6.5" r="6" fill="#fff"/><rect x="3" y="4.2" width="7" height="4.6" fill="var(--green)"/><path d="M3 4.2l3.5 2.6L10 4.2" fill="none" stroke="#fff" stroke-width=".8"/></svg>
      hello@brightacrebuilds.com
    </span>
    <span class="item">
      <svg viewBox="0 0 13 13"><circle cx="6.5" cy="6.5" r="5.6" fill="none" stroke="#fff" stroke-width="1.2"/><path d="M4.3 3.6l1.2 1.5-.6.8c.5 1 1.2 1.7 2.2 2.2l.8-.6 1.5 1.2-.7 1c-2.6-.4-4.7-2.5-5.1-5.1z" fill="#fff"/></svg>
      0123 456 789
    </span>
    <span class="item">
      <svg viewBox="0 0 13 13"><circle cx="6.5" cy="6.5" r="5.6" fill="none" stroke="#fff" stroke-width="1.2"/><circle cx="6.5" cy="6.5" r="3.2" fill="none" stroke="#fff" stroke-width=".9"/><path d="M1 6.5h11M6.5 1v11" stroke="#fff" stroke-width=".8"/></svg>
      www.BrightAcreBuilds.com
    </span>
  </footer>

</main>
</body>
</html>
```